Business Card Design

Brambledown Pantry is the name of my health coaching business. My tag line is "Everyday food for a well-lived life." I will be working with clients one-on-one and in groups. My target clients are women "of a certain age" who want to be more comfortable in their own skin. We will work together in a 6-month program. The coaching sessions will take place in my kitchen. I will also be conducting monthly cooking classes and field trips - to farmer's markets, speciality markets etc.. for my clients.
Updates

the business name is Brambledown Pantry - I'm not sure how the p got in there at the end of the name

Thank you

Please include the website - www.brambledownpantry-example.com and the tag line:

Everyday food for a well-lived life on the business card.

Thank you

Please add the phone number to the business card - sorry, I forgot to state that in the original brief

(555) 274-8150

Target Market(s)

Women "of a certain age" who want to be more comfortable in their own skin

Industry/Entity Type

Cooking

Contact Information for Business Card

Brambledown Pantry
Everyday food for a well-lived life

Rosalind Hartwell
Health Coach
(555) 274-8150

Font styles to use
Serif
Sans Serif

Requirements
Must have
• front & back design
I typical like soft colors - and have tended toward greens over time - I'm open although I would not like bright reds, yellows etc..

```html
<!DOCTYPE html>
<html lang="en">
<head>
<meta charset="UTF-8">
<title>Brambledown Pantry — Business Card</title>
<link href="https://fonts.googleapis.com/css2?family=Cinzel:wght@400&family=Comfortaa:wght@300;400&display=swap" rel="stylesheet">
<style>
  :root {
    --page-bg: #e6e8e4;
    --card-white: #ffffff;
    --card-shade: #eef0ec;
    --green: #6cb33f;
    --green-light: #8cc95a;
    --green-deep: #5ea233;
    --ink: #4a4a4a;
    --ink-soft: #6a6a6a;
    --rule: #c9ccc6;
    --on-green: #ffffff;
  }
  * { margin: 0; padding: 0; box-sizing: border-box; }
  html, body {
    width: 1200px; height: 822px; overflow: hidden;
    background: var(--page-bg);
  }
  .sheet {
    position: relative; width: 1200px; height: 822px;
    display: flex; flex-direction: column; align-items: center;
    justify-content: center; gap: 20px;
  }
  .card {
    position: relative; width: 660px; height: 377px; overflow: hidden;
    background: var(--card-white);
    box-shadow: 0 6px 18px rgba(0,0,0,0.18);
  }

  /* shared brand lockup */
  .brand-name {
    font-family: "Cinzel", "Times New Roman", serif;
    font-weight: 400; font-size: 44px; letter-spacing: 1px;
    color: var(--ink); line-height: 1; white-space: nowrap;
  }
  .brand-tagline {
    font-family: "Comfortaa", "Century Gothic", sans-serif;
    font-weight: 300; font-size: 19px; letter-spacing: 1.5px;
    color: var(--ink-soft); line-height: 1; margin-top: 6px; white-space: nowrap;
  }

  /* back */
  .card--back .band-top {
    position: absolute; left: 0; top: 0; width: 100%; height: 118px;
    background: linear-gradient(180deg, var(--green-light), var(--green));
  }
  .card--back .band-middle {
    position: absolute; left: 0; top: 118px; width: 100%; height: 112px;
    background: linear-gradient(180deg, var(--card-white), var(--card-shade));
    display: flex; flex-direction: column; align-items: center; justify-content: center;
  }
  .card--back .band-bottom {
    position: absolute; left: 0; top: 230px; width: 100%; height: 147px;
    background: linear-gradient(180deg, var(--green), var(--green-deep));
  }

  /* front */
  .card--front .brand {
    position: absolute; left: 82px; top: 64px;
  }
  .card--front .rule {
    position: absolute; left: 0; top: 200px; width: 100%; height: 2px;
    background: var(--rule);
  }
  .card--front .contact-band {
    position: absolute; left: 0; top: 206px; width: 100%; height: 104px;
    background: linear-gradient(180deg, var(--green-light), var(--green));
    color: var(--on-green);
    font-family: "Comfortaa", "Century Gothic", sans-serif; font-weight: 400;
  }
  .contact-name {
    position: absolute; left: 34px; top: 16px; font-size: 19px;
  }
  .contact-phone {
    position: absolute; left: 34px; top: 46px; font-size: 19px;
    display: flex; align-items: center; gap: 10px;
  }
  .contact-email {
    position: absolute; right: 26px; top: 74px; font-size: 17px;
    display: flex; align-items: center; gap: 10px;
  }
  .contact-icon { width: 18px; height: 18px; flex: none; }
  .card--front .rule--bottom { top: 312px; }
  .website {
    position: absolute; left: 120px; top: 334px;
    font-family: "Comfortaa", "Century Gothic", sans-serif; font-weight: 400;
    font-size: 18px; color: var(--ink);
  }
</style>
</head>
<body>
<main class="sheet">

  <section class="card card--back" aria-label="Card back">
    <div class="band-top"></div>
    <div class="band-middle">
      <div class="brand-name">Brambledown Pantry</div>
      <div class="brand-tagline">Everyday food for a well-lived life</div>
    </div>
    <div class="band-bottom"></div>
  </section>

  <section class="card card--front" aria-label="Card front">
    <div class="brand">
      <div class="brand-name">Brambledown Pantry</div>
      <div class="brand-tagline">Everyday food for a well-lived life</div>
    </div>
    <div class="rule"></div>
    <div class="contact-band">
      <div class="contact-name">Rosalind Hartwell Health Coach</div>
      <div class="contact-phone">
        <svg class="contact-icon" viewBox="0 0 24 24" aria-hidden="true">
          <path fill="currentColor" d="M6.6 10.8a15.1 15.1 0 0 0 6.6 6.6l2.2-2.2a1 1 0 0 1 1-.25 11.4 11.4 0 0 0 3.6.57 1 1 0 0 1 1 1V20a1 1 0 0 1-1 1A17 17 0 0 1 3 4a1 1 0 0 1 1-1h3.5a1 1 0 0 1 1 1c0 1.250.2 2.46.57 3.6a1 1 0 0 1-.25 1z"/>
        </svg>
        <span>(555) 274-8150</span>
      </div>
      <div class="contact-email">
        <svg class="contact-icon" viewBox="0 0 24 24" aria-hidden="true">
          <rect x="2" y="5" width="20" height="14" fill="currentColor"/>
          <path d="M2 5l10 8 10-8" fill="none" stroke="#6cb33f" stroke-width="1.6"/>
        </svg>
        <span>rosalind@brambledownpantry-example.com</span>
      </div>
    </div>
    <div class="rule rule--bottom"></div>
    <div class="website">www.brambledownpantry-example.com</div>
  </section>

</main>
</body>
</html>
```